Clothing for elderly and disabled persons business card

I have seen a design on the Prism website with a partial hand holding a heart I would like that to be incorporated above the i in Willowmere
The colours should be either soft green and pinks.
The final design should communicate care, love, easy fit comfort clothing for the frail and disabled.

Willowmere
Gentle WearClothing

Target Market(s)

Nursing Homes, Elderly in care or just anyone with limited mobility

Industry/Entity Type

Clothing

Contact Information for Business Card

Willowmere Gentle Wear Clothing
Carol Hensley Owner Sales Consultant
Phone 0451 726 083 Fax 08 9627 4418
Email: willowmeregentlewear@examplemail.com

Requirements
Nice to have
• A hand holding a heart this must form part of the i in Willowmere, instead of the dot above the i I want the hand holding the heart.

```html
<!DOCTYPE html>
<html lang="en">
<head>
<meta charset="utf-8">
<title>Willowmere Gentle Wear Clothing – Business Card</title>
<link href="https://fonts.googleapis.com/css2?family=Arimo:wght@400&display=swap" rel="stylesheet">
<style>
  :root {
    --card-white: #ffffff;
    --leaf-green: #4fc94f;
    --leaf-green-soft: #dff5df;
    --blossom-pink: #f5a3c7;
    --band-pink: #ff9dca;
    --crop-black: #1a1a1a;
  }
  * { margin: 0; padding: 0; box-sizing: border-box; }
  html, body {
    width: 1200px;
    height: 742px;
    overflow: hidden;
    background: var(--card-white);
  }
  .card {
    position: relative;
    width: 1200px;
    height: 742px;
    background: var(--card-white);
    font-family: "Arimo", Arial, sans-serif;
    overflow: hidden;
  }
  .crop-marks {
    position: absolute;
    inset: 0;
  }
  .brand-band {
    position: absolute;
    left: 0;
    top: 652px;
    width: 1200px;
    height: 90px;
    background: var(--band-pink);
  }
  .brand-mark {
    position: absolute;
    left: 92px;
    top: 192px;
    width: 136px;
    height: 136px;
    border-radius: 50%;
    background: var(--leaf-green-soft);
  }
  .brand-name {
    position: absolute;
    left: 256px;
    top: 166px;
    width: 640px;
    color: var(--blossom-pink);
    font-size: 66px;
    font-weight: 400;
    line-height: 72px;
    white-space: nowrap;
  }
  .brand-name .line { display: block; }
  .brand-name .line--second { padding-left: 184px; }
  .contact {
    position: absolute;
    left: 629px;
    top: 378px;
    color: var(--leaf-green);
  }
  .contact__person {
    display: flex;
    align-items: center;
    white-space: nowrap;
  }
  .contact__name { font-size: 45px; }
  .contact__divider {
    display: inline-block;
    width: 2px;
    height: 40px;
    background: var(--leaf-green);
    margin: 0 18px 0 20px;
  }
  .contact__role { font-size: 33px; letter-spacing: 0.5px; }
  .contact__lines {
    list-style: none;
    margin-top: 73px;
  }
  .contact__line {
    display: flex;
    align-items: center;
    height: 45px;
    font-size: 30px;
    white-space: nowrap;
  }
  .contact__icon {
    width: 26px;
    height: 26px;
    margin-right: 28px;
    flex: none;
  }
  .contact__email {
    margin-top: 2px;
    font-size: 28px;
  }
</style>
</head>
<body>
  <div class="card">
    <svg class="crop-marks" width="1200" height="742" viewBox="0 0 1200 742" aria-hidden="true">
      <g stroke="var(--crop-black)" stroke-width="2">
        <line x1="45" y1="0" x2="45" y2="27"/>
        <line x1="0" y1="54" x2="22" y2="54"/>
        <line x1="1155" y1="0" x2="1155" y2="27"/>
        <line x1="1178" y1="54" x2="1200" y2="54"/>
        <line x1="0" y1="683" x2="22" y2="683"/>
        <line x1="45" y1="714" x2="45" y2="742"/>
        <line x1="1178" y1="683" x2="1200" y2="683"/>
        <line x1="1155" y1="714" x2="1155" y2="742"/>
      </g>
    </svg>

    <div class="brand-mark" role="img" aria-label="Willowmere Gentle Wear brand mark"></div>

    <h1 class="brand-name">
      <span class="line">Willowmere Gentle</span>
      <span class="line line--second">Wear Clothing</span>
    </h1>

    <section class="contact">
      <p class="contact__person">
        <span class="contact__name">Carol Hensley</span>
        <span class="contact__divider"></span>
        <span class="contact__role">OWNER</span>
      </p>
      <ul class="contact__lines">
        <li class="contact__line">
          <svg class="contact__icon" viewBox="0 0 26 26" aria-label="Phone">
            <g fill="none" stroke="var(--leaf-green)" stroke-width="2">
              <rect x="2" y="3" width="6" height="20" rx="1"/>
              <rect x="8" y="5" width="16" height="18" rx="1"/>
              <line x1="12" y1="10" x2="20" y2="10"/>
              <line x1="12" y1="14" x2="20" y2="14"/>
              <line x1="12" y1="18" x2="20" y2="18"/>
            </g>
          </svg>
          <span>0451 726 083 (sales consultant)</span>
        </li>
        <li class="contact__line">
          <svg class="contact__icon" viewBox="0 0 26 26" aria-label="Fax">
            <g fill="none" stroke="var(--leaf-green)" stroke-width="2">
              <path d="M7 3h9l3 3v8H7z"/>
              <rect x="2" y="14" width="22" height="9"/>
              <line x1="6" y1="19" x2="14" y2="19"/>
            </g>
          </svg>
          <span>08 9627 4418 (fax)</span>
        </li>
        <li class="contact__line contact__email">willowmeregentlewear@examplemail.com</li>
      </ul>
    </section>

    <div class="brand-band"></div>
  </div>
</body>
</html>
```